Chartered Professional Accounting Firm Needs a Business Card Design

We need a card design for an accounting firm based in Toronto, Ontario. The firm name is Lorne Patek Professional Corporation. The owner of the firm is a chartered professional accountant and a certified general accountant. Services of the firm include 60% tax preparation and consulting and 40% financial statements for corporation year-end. We would like a modern design. The color could be black, white, gray, blue or other color to bring more confidence to clients. The logo of the firm should be included in the design. Thanks
Updates

Name: Lorne Patek, CPA, CGA Address: 47 Marrow Creek Rd. Richmond Hill, ON K7T 5P3 Telephone: (416) 555-0142 Fax:(416) 555-0187 Email: lorne@lornepatek.example

Industry/Entity Type

Accounting

```html
<!DOCTYPE html>
<html lang="en">
<head>
<meta charset="utf-8">
<title>Lorne Patek Professional Corporation — Business Card</title>
<link rel="stylesheet" href="https://fonts.googleapis.com/css2?family=Cinzel:wght@400;700&display=swap">
<style>
  :root {
    --brand-blue: #2e378f;
    --paper-white: #ffffff;
    --shadow-gray: #7d7d7f;
    --tagline-gray: #808083;
  }
  html, body {
    margin: 0;
    padding: 0;
    width: 1200px;
    height: 686px;
    overflow: hidden;
    background: var(--brand-blue);
  }
  .card {
    position: relative;
    width: 1200px;
    height: 686px;
    overflow: hidden;
    background: var(--brand-blue);
    font-family: "Cinzel", serif;
    color: var(--paper-white);
  }
  .card__swoosh {
    position: absolute;
    inset: 0;
  }
  .owner {
    position: absolute;
    left: 94px;
    top: 62px;
    margin: 0;
  }
  .owner__name {
    display: block;
    font-size: 36px;
    font-weight: 400;
    letter-spacing: 3px;
    line-height: 1;
  }
  .owner__title {
    display: block;
    margin-top: 18px;
    font-size: 26px;
    letter-spacing: 3px;
    line-height: 1;
  }
  .contact {
    position: absolute;
    left: 94px;
    top: 420px;
    margin: 0;
    padding: 0;
    list-style: none;
    font-size: 33px;
    letter-spacing: 2.5px;
    line-height: 48px;
  }
  .firm {
    position: absolute;
    left: 585px;
    top: 78px;
    display: flex;
    align-items: center;
    gap: 22px;
  }
  .firm__square {
    width: 92px;
    height: 92px;
    background: var(--brand-blue);
    flex: none;
  }
  .firm__text {
    display: flex;
    flex-direction: column;
  }
  .firm__name {
    margin: 0;
    color: var(--brand-blue);
    font-weight: 700;
    line-height: 1;
  }
  .firm__name-main {
    display: block;
    font-size: 46px;
    letter-spacing: 1px;
  }
  .firm__name-sub {
    display: block;
    margin-top: 4px;
    font-size: 21px;
    letter-spacing: 0.5px;
  }
  .firm__credentials {
    margin: 6px 0 0;
    color: var(--tagline-gray);
    font-size: 17px;
    letter-spacing: 1.2px;
    line-height: 22px;
  }
</style>
</head>
<body>
  <main class="card">
    <svg class="card__swoosh" width="1200" height="686" viewBox="0 0 1200 686" aria-hidden="true">
      <circle cx="918" cy="72" r="444" fill="var(--shadow-gray)"/>
      <circle cx="908" cy="58" r="440" fill="var(--paper-white)"/>
      <circle cx="908" cy="44" r="426" fill="var(--brand-blue)"/>
      <circle cx="906" cy="36" r="420" fill="var(--paper-white)"/>
    </svg>

    <h1 class="owner">
      <span class="owner__name">Lorne Patek</span>
      <span class="owner__title">Owner</span>
    </h1>

    <ul class="contact">
      <li class="contact__street">123 Address Lane</li>
      <li class="contact__city">Toronto, Canada</li>
      <li class="contact__phone">000.000.0000</li>
      <li class="contact__web">www.webaddress.com</li>
    </ul>

    <div class="firm">
      <div class="firm__square" aria-hidden="true"></div>
      <div class="firm__text">
        <p class="firm__name">
          <span class="firm__name-main">LORNE PATEK</span>
          <span class="firm__name-sub">PROFESSIONAL CORPORATION</span>
        </p>
        <p class="firm__credentials">CHARTERED PROFESSIONAL ACCOUNTANT<br>CERTIFIED GENERAL ACCOUNTANT</p>
      </div>
    </div>
  </main>
</body>
</html>
```